Commercial Construction Interior Fitout company needs Logo and Business Cards

We need a logo and business card design. We specialise in Commercial Ceilings, Partitions, Plastering and Carpentry.

Company name: 7QX Commercial Interiors. Would like a professional looking card more than a fancy look. Gloss front preferably black pattern with Fluro Green and white text.

Will need:

Name
Position
Phone
Fax
Email
Postal Address
Web address
Updates

Thank you so much everyone for your efforts and fantastic designs..   If I didn't respond to everyone personally,  my apologises. 

Again, thanks all

R.M                               

Target Market(s)

Existing & New clients in the Construction Industry

Industry/Entity Type

Business

Requirements
Nice to have
• 7QX to be overlapped or made into some sort of Logo

```html
<!DOCTYPE html>
<html lang="en">
<head>
<meta charset="utf-8">
<title>7QX Commercial Interiors – Business Card</title>
<link rel="stylesheet" href="https://fonts.googleapis.com/css2?family=Source+Sans+3:wght@400;600&family=Noto+Sans+Mono:wght@400&display=swap">
<style>
  :root {
    --card-black: #000000;
    --panel-black: #050505;
    --fluro-green: #8dc63f;
    --text-white: #ffffff;
    --rule-grey: #2a2a2a;
    --facet-grey: rgba(120, 120, 120, 0.45);
    --pattern-dark: #0c0c0c;
    --pattern-mid: #1e1e1e;
  }
  html, body {
    margin: 0;
    padding: 0;
    width: 1200px;
    height: 733px;
    overflow: hidden;
    background: var(--card-black);
  }
  .card {
    position: relative;
    width: 1200px;
    height: 733px;
    background: var(--card-black);
    font-family: "Source Sans 3", sans-serif;
    overflow: hidden;
  }
  .card-face {
    position: absolute;
    left: 0;
    top: 0;
    width: 1200px;
    height: 603px;
    background: var(--panel-black);
  }
  .card-face svg {
    position: absolute;
    left: 0;
    top: 0;
  }
  .brand {
    position: absolute;
    left: 112px;
    top: 92px;
    display: flex;
    align-items: center;
    gap: 14px;
    color: var(--text-white);
    font-size: 37px;
    font-weight: 600;
    line-height: 1;
    white-space: nowrap;
  }
  .brand-mark {
    width: 22px;
    height: 22px;
    background: var(--fluro-green);
  }
  .contact-block {
    position: absolute;
    left: 137px;
    top: 232px;
    height: 316px;
    border-left: 2px solid var(--rule-grey);
    padding-left: 29px;
  }
  .person-name {
    margin: 0;
    color: var(--fluro-green);
    font-size: 40px;
    font-weight: 400;
    line-height: 1;
    margin-top: 0;
  }
  .person-position {
    margin: 8px 0 0;
    color: var(--fluro-green);
    font-size: 29px;
    font-weight: 400;
    line-height: 1;
  }
  .contact-list {
    list-style: none;
    margin: 76px 0 0;
    padding: 0;
    color: var(--text-white);
    font-family: "Noto Sans Mono", monospace;
    font-size: 31px;
    line-height: 48px;
    letter-spacing: 1px;
  }
  .web-tab {
    position: absolute;
    left: 86px;
    top: 638px;
    width: 1018px;
    height: 87px;
    background: var(--fluro-green);
    border-radius: 42px 42px 0 0;
    display: flex;
    align-items: center;
    justify-content: center;
    color: var(--card-black);
    font-size: 36px;
    font-weight: 400;
  }
</style>
</head>
<body>
<div class="card">
  <div class="card-face">
    <svg width="1200" height="603" viewBox="0 0 1200 603">
      <defs>
        <linearGradient id="pattern-tone" x1="0" y1="0" x2="1" y2="0.3">
          <stop offset="0" stop-color="#050505"/>
          <stop offset="0.4" stop-color="#0c0c0c"/>
          <stop offset="1" stop-color="#222222"/>
        </linearGradient>
      </defs>
      <rect x="300" y="0" width="900" height="603" fill="url(#pattern-tone)" role="img" aria-label="Dark hexagon mesh pattern with falling light streaks"/>
      <polygon class="facet facet-top" points="838,0 1200,0 1200,18 1042,176" fill="var(--facet-grey)"/>
      <polyline points="960,0 1030,80 1085,0" fill="none" stroke="var(--fluro-green)" stroke-width="2"/>
      <polygon class="facet facet-side" points="990,405 1200,195 1200,603 1188,603" fill="var(--facet-grey)"/>
      <polyline points="1200,352 1110,410 1200,470" fill="none" stroke="var(--fluro-green)" stroke-width="2"/>
    </svg>
  </div>

  <div class="brand">
    <span class="brand-mark"></span>
    <span class="brand-name">7QX Commercial interiors</span>
  </div>

  <div class="contact-block">
    <h1 class="person-name">Your Name</h1>
    <p class="person-position">Position</p>
    <ul class="contact-list">
      <li>Phone:</li>
      <li>Fax:</li>
      <li>Email:</li>
      <li>Postal Address</li>
    </ul>
  </div>

  <div class="web-tab">Web address</div>
</div>
</body>
</html>
```